Bluefern Healthplan

We're designing a website to sell Medicare Supplements. Attached is an image of the words we want to say and general layout, but please use your best knowledge to make it better. This platform is intentionally simplistic because this is reaching an older demographic, so it should be very straightforward, attention-grabbing and extremely user-friendly, while still appearing reliable and professional.
Use your best judgement for color palate that conveys professional but approachable. Feel free to add imagery but don't overwhelm the page.
Updates
Designs look the same
Target Market(s)
65+ seniors
Number of Pages Required
1 page
Look and feel

```html
<!DOCTYPE html>
<html lang="en">
<head>
<meta charset="utf-8">
<title>Bluefern Healthplan</title>
<link href="https://fonts.googleapis.com/css2?family=Poppins:wght@300;400;500;600;700&display=swap" rel="stylesheet">
<style>
:root{
  --purple:#3b3878;
  --purple-dark:#2f2c66;
  --purple-soft:#4d4a8c;
  --pink:#e63f78;
  --yellow:#f7d417;
  --ink:#2b2b3a;
  --muted:#8a8a9a;
  --line:#e4e4ec;
  --bg-soft:#f3f5f9;
  --white:#ffffff;
  --placeholder:#d9d9d9;
}
*{box-sizing:border-box;margin:0;padding:0}
html,body{width:1200px;height:3764px;overflow:hidden}
body{font-family:"Poppins",Arial,sans-serif;color:var(--ink);background:var(--white);position:relative}
section,header,footer{position:absolute;left:0;width:1200px}

/* header */
.site-header{top:0;height:80px;background:var(--white)}
.brand{position:absolute;left:40px;top:14px}
.brand-name{display:flex;align-items:center;gap:10px;font-size:30px;font-weight:600;color:var(--purple);letter-spacing:.5px}
.brand-dot{width:30px;height:30px;border-radius:50%;background:var(--purple)}
.brand-tag{font-size:11px;color:var(--muted);margin-left:40px;margin-top:-2px}
.main-nav{position:absolute;right:40px;top:26px;display:flex;gap:22px;align-items:center;font-size:15px}
.main-nav a{color:var(--ink);text-decoration:none}
.main-nav .nav-call{font-size:22px;font-weight:500;color:var(--purple)}

/* hero */
.hero{top:80px;height:480px;background:var(--purple);color:var(--white);text-align:center}
.hero-art{position:absolute;top:40px;width:330px;height:400px;border-radius:20px;background:linear-gradient(160deg,rgba(255,255,255,.14),rgba(255,255,255,.04))}
.hero-art.left{left:0}
.hero-art.right{right:0}
.hero-title{position:relative;margin-top:58px;font-size:48px;font-weight:700;letter-spacing:.5px}
.hero-sub{font-size:19px;margin-top:6px}
.quote-form{display:flex;justify-content:center;margin-top:22px}
.quote-form .field{width:492px;height:52px;background:var(--white);color:#aaa;font-size:13px;text-align:left;padding:18px 16px}
.quote-form .go{width:96px;height:52px;background:#111;color:var(--white);font-size:15px;font-weight:500;line-height:52px}
.hero-or{font-size:17px;margin-top:16px}
.hero-call{font-size:62px;font-weight:700;line-height:1.1;margin-top:4px}
.hero-note{font-size:19px}

/* section headings */
.section-title{text-align:center;font-size:38px;font-weight:400;color:var(--ink);letter-spacing:.5px}
.section-title strong{color:var(--purple);font-weight:600}
.section-lead{width:720px;margin:8px auto 0;text-align:center;font-size:17px;color:var(--muted);line-height:1.45}

/* understanding */
.understanding{top:560px;height:760px;background:var(--white);padding-top:106px}
.steps{position:absolute;top:240px;left:100px;width:992px;height:300px}
.step{position:absolute;top:0;width:310px;height:300px;background:var(--white);box-shadow:0 4px 18px rgba(40,40,90,.13);text-align:center;padding-top:42px}
.step:nth-child(1){left:0}
.step:nth-child(2){left:346px}
.step:nth-child(3){left:682px}
.step-art{width:100px;height:100px;margin:0 auto;border-radius:12px;background:linear-gradient(135deg,#e8e9f6,#cfd2ef)}
.step h3{font-size:17px;font-weight:600;color:var(--pink);margin-top:22px}
.step p{font-size:12px;color:var(--muted);width:220px;margin:8px auto 0;line-height:1.5}
.step-arrow{position:absolute;top:134px;width:32px;height:32px}
.cta{position:absolute;top:620px;left:452px;width:288px;height:46px;border-radius:23px;background:var(--pink);color:var(--white);font-size:15px;font-weight:500;text-align:center;line-height:46px}

/* featured */
.featured{top:1320px;height:680px;background:var(--bg-soft);padding-top:92px}
.slide{position:absolute;background:var(--placeholder);color:#bbb;font-size:22px;display:flex;align-items:center;justify-content:center}
.slide.far-l{left:100px;top:232px;width:100px;height:268px}
.slide.near-l{left:240px;top:232px;width:208px;height:268px}
.slide.center{left:472px;top:200px;width:248px;height:340px;background:#c9c9c9;color:#999;box-shadow:0 8px 22px rgba(0,0,0,.18)}
.slide.near-r{left:744px;top:232px;width:208px;height:268px}
.slide.far-r{left:992px;top:232px;width:108px;height:268px}
.slide-badge{position:absolute;right:12px;top:12px;display:flex;gap:4px}
.slide-badge span{width:26px;height:14px;background:var(--purple)}
.slide-caption{position:absolute;left:50px;bottom:0;width:148px;height:56px;background:var(--purple);color:var(--white);font-size:12px;padding:9px 12px;line-height:1.35}
.slide-caption b{display:block;font-weight:600}
.dots{position:absolute;top:574px;left:0;width:1200px;display:flex;justify-content:center;gap:10px}
.dots span{width:9px;height:9px;border-radius:50%;background:#cfd0dc}
.dots span.on{background:var(--pink)}

/* coverage */
.coverage{top:2000px;height:920px;background:var(--bg-soft);padding-top:100px}
.finder{position:absolute;top:232px;width:320px;background:var(--white);box-shadow:0 4px 16px rgba(40,40,90,.12)}
.finder.city{left:268px}
.finder.care{left:608px}
.finder-head{height:128px;background:var(--purple);color:#49d3b4;text-align:center;font-size:14px;font-weight:500;padding-top:30px}
.finder-head svg{display:block;margin:0 auto 10px}
.finder-list{list-style:none}
.finder-list li{height:45px;border-bottom:1px solid var(--line);display:flex;align-items:center;padding:0 14px;font-size:13px;color:#555}
.finder-list li::before{content:"";width:14px;height:14px;border:1px solid #c6c6d2;margin-right:16px}
.finder-list li::after{content:"";margin-left:auto;width:6px;height:6px;border-right:1.5px solid #aaa;border-bottom:1.5px solid #aaa;transform:rotate(45deg)}
.finder-list li.active{background:var(--pink);color:var(--white)}
.finder-list li.active::before{border-color:var(--white)}
.finder-list li.active::after{border-color:var(--white)}

/* help */
.help{top:2920px;height:640px;background:var(--purple);color:var(--white)}
.help-photo{position:absolute;left:120px;top:80px;width:400px;height:400px;background:linear-gradient(135deg,#d6d6d6,#bdbdbd);color:#a8a8a8;font-size:48px;display:flex;align-items:center;justify-content:center}
.help-title{position:absolute;left:588px;top:92px;font-size:34px;font-weight:600}
.help-title span{color:var(--yellow)}
.help-text{position:absolute;left:588px;top:146px;width:460px;font-size:16px;line-height:1.45;color:#e2e2f0}
.help-arrow{position:absolute;left:540px;top:260px}
.help-phone{position:absolute;left:588px;top:262px;font-size:40px;font-weight:600}

/* footer */
.site-footer{top:3560px;height:204px;background:var(--white)}
.foot-brand{position:absolute;left:100px;top:44px;font-size:24px;font-weight:700;color:var(--purple);line-height:1.1}
.foot-col{position:absolute;top:40px;font-size:11px;color:#666;line-height:1.9}
.foot-col h4{font-size:11px;font-weight:500;color:#999;margin-bottom:4px;letter-spacing:.5px}
.foot-col.about{left:352px}
.foot-col.links{left:604px}
.foot-col.contact{left:864px}
.contact-row{display:flex;align-items:center;gap:8px}
.contact-row i{width:8px;height:8px;background:var(--pink);border-radius:2px}
.socials{display:flex;gap:14px;margin-top:4px}
.socials span{width:14px;height:14px;border-radius:50%;background:#444}
.foot-bottom{position:absolute;left:100px;right:100px;top:152px;border-top:1px solid var(--line);padding-top:12px;font-size:11px;color:#999;display:flex;justify-content:space-between}
.to-top{position:absolute;right:10px;top:160px;width:30px;height:30px;background:#333}
.to-top svg{display:block;margin:9px auto}
</style>
</head>
<body>

<header class="site-header">
  <div class="brand">
    <div class="brand-name"><span class="brand-dot"></span>Bluefern Healthplan</div>
    <div class="brand-tag">Be confident in choosing the Medicare Supplement plan that's right for you.</div>
  </div>
  <nav class="main-nav">
    <a href="#">Home</a>
    <a href="#">Get In Touch</a>
    <a href="#" class="nav-call">Call Us: (800) 555-0142</a>
  </nav>
</header>

<section class="hero">
  <div class="hero-art left" role="img" aria-label="Illustration of a clipboard, pills and a thermometer"></div>
  <div class="hero-art right" role="img" aria-label="Illustration of an envelope, stethoscope and medicine bottle"></div>
  <h1 class="hero-title">FREE MEDICAID INSURANCE QUOTE</h1>
  <p class="hero-sub">Our easy tool lets you compare quotes from top providers, all at once!</p>
  <div class="quote-form"><div class="field">Zipcode</div><div class="go">Search</div></div>
  <p class="hero-or">OR</p>
  <p class="hero-call">CALL: (800) 555-0142</p>
  <p class="hero-note">And talk to a live agent to help you find the right plan!</p>
</section>

<section class="understanding">
  <h2 class="section-title">UNDERSTANDING <strong>MEDICAID</strong></h2>
  <p class="section-lead">Usu habeo equidem sanctus ne. Suas summo id sed, erat erant oporteat cu pri. In eum omnes molestie. Sed ad debet scaevola ne mei.</p>
  <div class="steps">
    <div class="step">
      <div class="step-art" role="img" aria-label="Icon of a hospital building"></div>
      <h3>COVERAGE</h3>
      <p>Compare plans from trusted carriers and see what each one covers in plain words.</p>
    </div>
    <div class="step">
      <div class="step-art" role="img" aria-label="Icon of people getting help"></div>
      <h3>ACCESSIBILITY</h3>
      <p>Get help by phone or online whenever you need it, with no pressure to buy.</p>
    </div>
    <div class="step">
      <div class="step-art" role="img" aria-label="Icon of a phone showing plan details"></div>
      <h3>TRANSPARENT</h3>
      <p>Clear prices and honest answers so you always know exactly what you pay for.</p>
    </div>
    <svg class="step-arrow" style="left:317px" viewBox="0 0 32 32"><path d="M8 16h16M18 10l6 6-6 6" fill="none" stroke="#b5b5c5" stroke-width="2"/></svg>
    <svg class="step-arrow" style="left:657px" viewBox="0 0 32 32"><path d="M8 16h16M18 10l6 6-6 6" fill="none" stroke="#b5b5c5" stroke-width="2"/></svg>
  </div>
  <div class="cta">Browse Through Our Options</div>
</section>

<section class="featured">
  <h2 class="section-title">FEATURED OPTIONS</h2>
  <p class="section-lead">Usu habeo equidem sanctus ne. Suas summo id sed, erat erant oporteat cu pri.</p>
  <div class="slide far-l">360</div>
  <div class="slide near-l">360 x 360</div>
  <div class="slide center">360 x 360
    <div class="slide-badge"><span></span><span></span></div>
    <div class="slide-caption"><b>Includes Dental!</b>Save 40% per month</div>
  </div>
  <div class="slide near-r">360 x 360</div>
  <div class="slide far-r">360</div>
  <div class="dots"><span class="on"></span><span></span><span></span><span></span><span></span></div>
</section>

<section class="coverage">
  <h2 class="section-title">FIND YOUR PERFECT COVERAGE</h2>
  <p class="section-lead">Nec graeci adipiscing disputationi ex, mea ea nonumes percipitur. Nonumy ponderum oporteat cu mel, pro movet soluta at.</p>
  <div class="finder city">
    <div class="finder-head">
      <svg width="22" height="28" viewBox="0 0 22 28"><path d="M11 1C5.5 1 1 5.3 1 10.7 1 18 11 27 11 27s10-9 10-16.3C21 5.3 16.5 1 11 1z" fill="none" stroke="#fff" stroke-width="2"/><circle cx="11" cy="10.5" r="3.5" fill="none" stroke="#fff" stroke-width="2"/></svg>
      SEARCH BY CITY OR ZONE
    </div>
    <ul class="finder-list">
      <li class="active">Albany</li><li>Albuquerque</li><li>Atlanta</li><li>Baltimore</li><li>Baton Rouge</li><li>Birmingham</li><li>Boston</li><li>Buffalo</li><li>Charleston</li><li>More...</li>
    </ul>
  </div>
  <div class="finder care">
    <div class="finder-head">
      <svg width="28" height="28" viewBox="0 0 28 28"><circle cx="14" cy="14" r="12" fill="none" stroke="#fff" stroke-width="2"/><path d="M14 8v12M8 14h12" stroke="#fff" stroke-width="2"/></svg>
      SEARCH BY COVERAGE
    </div>
    <ul class="finder-list">
      <li>Allergist</li><li>Cardiologist</li><li>Chiropractor</li><li>Dentist</li><li>Dermatologist</li><li>Gastroenterologist</li><li>Ophthalmologist</li><li>Optometrist</li><li>Podiatrician</li><li>More...</li>
    </ul>
  </div>
</section>

<section class="help">
  <div class="help-photo" role="img" aria-label="Photo of a friendly support agent">565 x 565</div>
  <h2 class="help-title">Need Help? <span>Call Us</span> Now!</h2>
  <p class="help-text">Tota omittantur necessitatibus mei ei. Quo paulo perfecto eu, errem percipit ponderum no eos. Has eu mazim sensibus. Ad nonumes dissentiunt qui, ei menandri electram eos. Nam iisque consequuntur cu.</p>
  <svg class="help-arrow" width="44" height="60" viewBox="0 0 44 60"><path d="M6 4c-6 22 4 40 28 44" fill="none" stroke="#fff" stroke-width="2.5" stroke-linecap="round"/><path d="M28 40l8 8-10 5" fill="none" stroke="#fff" stroke-width="2.5" stroke-linecap="round"/></svg>
  <p class="help-phone">(800) 555-0142</p>
</section>

<footer class="site-footer">
  <div class="foot-brand">BLUEFERN<br>HEALTHPLAN</div>
  <div class="foot-col about">
    <h4>ABOUT</h4>
    About Us<br>Blog<br>FAQ<br>Get A Quote<br>Register
  </div>
  <div class="foot-col links"><h4>USEFUL LINKS</h4></div>
  <div class="foot-col contact">
    <h4>CONTACT DETAILS</h4>
    <div class="contact-row"><i></i>(800) 555-0142</div>
    <div class="contact-row"><i></i>hello@bluefernhealthplan.com</div>
    <h4 style="margin-top:6px">FOLLOW US</h4>
    <div class="socials"><span></span><span></span><span></span><span></span></div>
  </div>
  <div class="foot-bottom"><span>Terms and conditions &nbsp;|&nbsp; Privacy</span><span>©2020 Bluefern Healthplan</span></div>
  <div class="to-top"><svg width="12" height="10" viewBox="0 0 12 10"><path d="M1 8l5-6 5 6" fill="none" stroke="#fff" stroke-width="2"/></svg></div>
</footer>

</body>
</html>
```